Word Doc Design for construction report

We have a database that dumps all of this data into this word doc. We need a much more appealing, visually friendly document. I have attached the main document and the cover page.
You don't need to edited all the repeated pages, just give us a style guide. I have attached our branding.
Updates

Hi I have pulled together a final design and now just need someone to put it all into a word doc. The final document is 36 pages. I am prepared to pay the design fee listed plus a $200 tip, however, we need it delivered by Monday. Is there anyone available to do this work?

Requirements
Must have
• Be easy on the eye as there is a LOT of repeated content

```html
<!DOCTYPE html>
<html lang="en">
<head>
<meta charset="utf-8">
<title>ACT Maintenance Plan – Style Guide Spread</title>
<link href="https://fonts.googleapis.com/css2?family=Open+Sans:wght@400;600;700&family=Poppins:wght@300;400&display=swap" rel="stylesheet">
<style>
:root{
  --blue:#0b87c9;
  --teal:#12aa9a;
  --navy:#23356b;
  --lime:#c6da55;
  --line:#c9d2da;
  --ink:#2b2f36;
  --muted:#6b7480;
}
*{box-sizing:border-box;margin:0;padding:0}
html,body{width:1124px;height:1200px;overflow:hidden;background:#fff}
body{font-family:'Open Sans',sans-serif;color:var(--ink)}
.canvas{position:relative;width:1124px;height:1200px}

.page{position:absolute;background:#fff;overflow:hidden;box-shadow:0 0 0 .6px #8e9aa6}
.page--land{width:328px;height:232px}
.page--port{width:232px;height:328px}

.page-head{position:absolute;left:0;right:0;top:0;height:27px;background:var(--blue)}
.page-logo{position:absolute;left:7px;top:-5px;width:46px;height:38px;border-radius:50%;background:#fff;display:flex;flex-direction:column;align-items:center;justify-content:center;padding-top:4px;font-size:4.4px;font-weight:600;color:var(--navy);line-height:1.15;text-align:center}
.page--port .page-logo{left:4px;width:44px}
.page-title{position:absolute;right:12px;top:21px;font-size:3.3px;font-weight:600;color:#fff}
.page-foot{position:absolute;left:0;right:0;bottom:0;height:13px;background:var(--teal);display:flex;align-items:center;justify-content:center;font-size:2.6px;color:#fff}
.page-num{position:absolute;right:9px;top:2px;height:9px;padding:0 4px;border-radius:5px;background:#fff;color:var(--ink);font-size:2.6px;line-height:9px}

.sec{position:absolute;left:15px;right:15px}
.page--port .sec{left:14px;right:14px}
.sec-title{display:inline-block;background:var(--teal);color:#fff;font-size:5.4px;font-weight:600;letter-spacing:.1px;padding:1.3px 7px 1.3px 8px;clip-path:polygon(4px 0,100% 0,100% 100%,0 100%);margin-bottom:2.5px;box-shadow:inset 0 -0.8px 0 #0d8a7d}
.label{font-size:2.4px;color:var(--muted);margin:2.5px 0 1px}
.body-text{font-size:2.4px;line-height:1.45;color:var(--ink)}
.body-text + .body-text{margin-top:2px}

.life{margin-bottom:1px}
.life-head,.life-row{display:grid;grid-template-columns:18% repeat(16,1fr)}
.life-head{background:var(--blue);color:#fff;font-size:2.7px;height:6px;align-items:center}
.life-head b{font-weight:600;padding-left:1.5px}
.life-head i{font-style:normal;text-align:center}
.life-note{font-size:1.7px;color:var(--muted);padding:.6px 1.5px;border-left:.4px solid var(--line);border-right:.4px solid var(--line)}
.life-row{height:7px;border:.4px solid var(--line);border-top:none}
.life-row b{font-size:2.7px;font-weight:600;color:var(--blue);padding-left:1.5px;align-self:center}
.life-row i{border-left:.4px solid var(--line);position:relative}
.life-row i.tick::before{content:"";position:absolute;left:50%;top:50%;width:4px;height:4px;margin:-2px 0 0 -2px;border:.5px solid var(--teal)}
.life-row i.tick::after{content:"";position:absolute;left:50%;top:50%;width:1.3px;height:2.6px;margin:-1.8px 0 0 -.6px;border:solid var(--teal);border-width:0 .6px .6px 0;transform:rotate(45deg)}

.grid-table{width:100%;border-collapse:collapse;font-size:2.6px;table-layout:fixed}
.grid-table th{background:var(--blue);color:#fff;font-weight:600;text-align:left;padding:1px 1.5px;border-right:.4px solid #fff;height:6px;vertical-align:top}
.grid-table td{padding:1px 1.5px;border:.4px solid var(--line);height:6px;vertical-align:top}
.grid-table--teal th{background:var(--teal)}

.super{position:absolute;right:13px;top:9px;width:103px}
.super-title{font-size:5.2px;color:#fff;font-weight:600;text-align:center;margin-bottom:2px}
.super-row{display:grid;grid-template-columns:47% 53%;font-size:2.7px;height:6.2px;align-items:center}
.super-row span:first-child{background:var(--teal);color:#fff;height:100%;padding:0 1.5px;display:flex;align-items:center;border-bottom:.4px solid #fff}
.super-row span:last-child{background:#fff;padding:0 1.5px;height:100%;display:flex;align-items:center;border-bottom:.4px solid var(--line)}

.defs{display:grid;grid-template-columns:44px 1fr;font-size:2.4px;row-gap:.6px;margin-top:1px}
.defs dt{font-weight:600}

/* cover */
.cover{left:47px;top:49px;width:232px;height:327px}
.cover-band{position:absolute;top:0;left:0;right:0;height:13px;display:grid;grid-template-columns:119px 1fr}
.cover-band span:first-child{background:var(--blue)}
.cover-band span:last-child{background:var(--teal)}
.cover-brand{position:absolute;left:8px;top:34px;font-size:15px;font-weight:600;color:var(--navy);line-height:1.05}
.cover-panel{position:absolute;left:83px;right:0;top:85px;height:81px;background:var(--blue);padding:8px 0 0 7px;color:#fff}
.cover-panel h1{font-size:18px;font-weight:700;line-height:.98;letter-spacing:-.2px}
.cover-rule{width:50px;height:1px;background:#fff;margin:3px 0 5px}
.cover-date{font-family:'Poppins',sans-serif;font-weight:300;font-size:6px}
.cover-photo{position:absolute;left:0;top:166px;width:211px;height:112px;background:linear-gradient(180deg,#cfe3ef 0%,#e9eef0 30%,#9fb8a4 55%,#4f7f3d 80%,#3f6a2b 100%)}
.cover-accent{position:absolute;left:211px;top:232px;width:14px;height:46px;background:var(--teal)}
.cover-site{position:absolute;left:10px;top:295px;font-family:'Poppins',sans-serif;font-weight:300;font-size:5.2px;line-height:1.35;color:var(--ink)}
.cover-contact{position:absolute;right:7px;top:287px;font-family:'Poppins',sans-serif;font-weight:300;font-size:5.2px;line-height:1.38;text-align:right;color:var(--ink)}
.cover-foot{position:absolute;left:0;right:0;bottom:0;height:12px;background:var(--lime)}

/* portal page */
.portal{position:absolute;left:10px;right:11px;top:45px;height:43px;background:var(--blue);color:#fff;padding:4px 5px}
.portal h2{font-size:5px;font-weight:400;margin-bottom:3px}
.portal p{font-size:2.6px;line-height:1.45}
.summary{position:absolute;left:14px;right:14px;top:121px}
.summary-row{display:grid;grid-template-columns:65px 1fr;font-size:2.8px;height:10.3px;align-items:center;border-bottom:.5px solid #9aa4ae}
.summary-row b{font-weight:600}
.summary-row.gap{margin-top:6px}

.scope-title{font-size:6.4px;color:var(--teal);font-weight:400;margin-bottom:3px}
.scope-list{list-style:none;font-size:2.4px;font-weight:600;margin:2px 0 3px 8px}
.scope-list li::before{content:"•";color:var(--teal);margin:0 2px 0 -5px}
.notice{background:var(--teal);color:#fff;font-size:2.4px;line-height:1.45;padding:1.5px 2px;margin:3px 0}
.sign{position:absolute;left:20px;right:20px;top:218px;display:grid;grid-template-columns:1fr 1fr;row-gap:7px;font-size:2.8px}
.badges{position:absolute;left:20px;right:20px;top:272px;display:flex;justify-content:space-between;align-items:center}
.badge-a{width:60px;height:26px;border-radius:3px;background:#dff1ef}
.badge-b{width:38px;height:18px;background:#2f8a3d}
.badge-c{width:20px;height:20px;background:#f2a33a}

.map{position:absolute;left:26px;width:180px;height:95px;top:77px;background:linear-gradient(135deg,#dbe9cf 0%,#c9e0c0 40%,#8fc1e6 55%,#d6e8cc 70%,#eef1ea 100%)}
.sat{position:absolute;left:26px;width:180px;height:105px;top:190px;background:radial-gradient(circle at 55% 50%,#8a8d84 0%,#5e6a55 45%,#3e4b39 100%)}
</style>
</head>
<body>
<main class="canvas">

<!-- Cover -->
<section class="page cover">
  <div class="cover-band"><span></span><span></span></div>
  <div class="cover-brand">Keystone<br>Survey</div>
  <div class="cover-panel">
    <h1>ACT<br>Maintenance<br>Plan</h1>
    <div class="cover-rule"></div>
    <div class="cover-date">12 April 2022</div>
  </div>
  <div class="cover-photo" role="img" aria-label="Photograph of a modern multi-storey apartment building with balconies behind a green lawn and trees"></div>
  <div class="cover-accent"></div>
  <div class="cover-site">Units Plan 812<br>8 of 40 Ridgeview Road Canberra 2601</div>
  <div class="cover-contact">keystonesurvey.example<br>12 Wattle Lane<br>Bruce ACT 2617<br>p 6200 0000</div>
  <div class="cover-foot"></div>
</section>

<!-- Page 1 -->
<section class="page page--port" style="left:312px;top:50px">
  <div class="page-head"><div class="page-logo">Keystone<br>Survey</div><div class="page-title">ACT Maintenance Plan - 2022</div></div>
  <div class="portal">
    <h2>Keystone Survey Strata Maintenance Portal</h2>
    <p>Your Strata Manager at [[X Strata Group]] and the Executive Committee for the Owners Corporation have been provided with access to the Keystone Survey Strata Maintenance Portal StrataVault. This resource gives access to the Building File for [[StreetAddress]] [[Suburb]] and includes a full photo log, your Maintenance Plan, Anticipated Capital Expenditure Plan and important maintenance logs and service reminders on the common property.</p>
  </div>
  <div class="sec" style="top:104px"><div class="sec-title">REPORT SUMMARY</div></div>
  <div class="summary">
    <div class="summary-row"><b>CLIENT</b><span>[[ClientName]]</span></div>
    <div class="summary-row"><b>BUILDING LOCATION</b><span>[[StreetAddress]] [[Suburb]]</span></div>
    <div class="summary-row"><b>BLOCK NUMBER</b><span>[[BLOCK]]</span></div>
    <div class="summary-row"><b>SECTION NUMBER</b><span>[[SECTION]]</span></div>
    <div class="summary-row"><b>SCHEME NUMBER</b><span></span></div>
    <div class="summary-row gap"><b>INSPECTION DATE</b><span>[[InspectionDate|d mmmm yyyy]]</span></div>
    <div class="summary-row"><b>INSPECTOR</b><span>[[Inspector]]</span></div>
    <div class="summary-row"><b>WEATHER CONDITIONS</b><span>[[Summary of Property Details|weather conditions|ItemValue]]</span></div>
    <div class="summary-row gap"><b>STRATAVAULT FILE NUMBER</b><span>[[JobNumber]]</span></div>
  </div>
  <div class="sec" style="top:231px">
    <p class="body-text">The Unit Titles (Management) Act 2011 and associated regulations set the framework for managing multi-unit residential properties. All Owners Corporations are required to hold a Maintenance Plan, taking into account the Developers Maintenance Schedule (if any). The Executive Committee then references this plan as part of their duty for overseeing maintenance of the common property. The Owners Corporation should review their plan regularly and amend where necessary. A full database of building elements, repair or replacement works, systems, equipment, structures and other items, including copies of manuals and warranty information, is registered in StrataVault.</p>
    <p class="body-text">Following preparation of our project file for [[StreetAddress]] [[Suburb]], which included reviewing materials such as maintenance schedules, sinking fund reports, warranties and manufacturer recommendations, our Building Inspector conducted a full on-site visual inspection on [[InspectionDate|d mmmm yyyy]]. If detailed information on plant and equipment and common areas was not made available or not visible on the day, the StrataVault file for this building will be updated by [[X strata manager]] and the Executive Committee as required. It is critical this Maintenance Plan is monitored and updated on an ongoing basis to keep systems, equipment and structures of the common property in good working order and to avoid costly reactive repairs.</p>
  </div>
  <div class="page-foot">[[StreetAddress]] [[Suburb]] - COPYRIGHT: Keystone Survey<span class="page-num">Page 1</span></div>
</section>

<!-- Page 2 -->
<section class="page page--port" style="left:572px;top:50px">
  <div class="page-head"><div class="page-logo">Keystone<br>Survey</div><div class="page-title">ACT Maintenance Plan - 2022</div></div>
  <div class="sec" style="top:46px">
    <h2 class="scope-title">Project Scope</h2>
    <p class="body-text">This Maintenance Plan has been compiled to help the Property meet its obligations under the following legislation (both as amended 1 November 2020):</p>
    <ul class="scope-list"><li>Unit Titles (Management) Act 2011 (s24)</li><li>Unit Titles (Management) Regulation 2011 (s4A)</li></ul>
    <p class="body-text">Documents supplied as part of the Developer's Maintenance Schedule and other reference material</p>
    <ul class="scope-list"><li>Drop downs</li><li>ACT Building Services Multi-unit Residential Building Maintenance Guide</li></ul>
    <p class="body-text">Manuals, warranties and sundry maintenance statements</p>
    <ul class="scope-list"><li>All documentation supplied by the Strata Group referenced while compiling this Maintenance Plan has been saved against the Strata File in the Keystone Survey Strata Maintenance Portal.</li></ul>
    <p class="body-text">Building Class</p>
    <ul class="scope-list"><li>X</li></ul>
    <p class="body-text">In typical Class A Units Plans, the unit owner owns the inside of the unit but not the main structure of the building. Usually, the individual owner owns from the inside of their lot to halfway through the boundary walls, ceiling and floor. In general, the owners corporation owns the walls, ceiling and floor from outside of the lot to halfway in. Internal walls within the unit, floor coverings, light fittings and curtains are all property of the unit owner.</p>
    <p class="notice">IMPORTANT: This report is intended to be read in its entirety. It has been commissioned to satisfy the requirements of 4A Maintenance plan – Act s 24 (3); Unit Titles Management Regulation 2011. The appropriate Strata Group Representative or Members of the Body Corporate Executive are asked to contact our company if any of the report's content is not fully understood and requires further explanation.</p>
    <p class="body-text"><b>Please refer to important Scope and Limitations at the end of this document</b></p>
    <p class="body-text">Thank you for the opportunity to work with you on this project, please do not hesitate to contact our team.</p>
  </div>
  <div class="sign">
    <span>[[Summary of Property Details</span><span>[[Summary of Property Details</span>
    <span>SIGNATURE</span><span>SIGNATURE</span>
    <span>[image100@100]]</span><span>itemvalue]]</span>
  </div>
  <div class="badges">
    <span class="badge-a" role="img" aria-label="Charity partner badge"></span>
    <span class="badge-b" role="img" aria-label="Industry association badge"></span>
    <span class="badge-c" role="img" aria-label="Builders association member badge"></span>
  </div>
  <div class="page-foot">[[StreetAddress]] [[Suburb]] - COPYRIGHT: Keystone Survey<span class="page-num">Page 2</span></div>
</section>

<!-- Page 3 -->
<section class="page page--port" style="left:829px;top:50px">
  <div class="page-head"><div class="page-logo">Keystone<br>Survey</div><div class="page-title">ACT Maintenance Plan - 2022</div></div>
  <div class="sec" style="top:48px"><p class="body-text" style="font-size:3px">A comprehensive photo log of all pictures captured during the maintenance plan inspection on 2 May 2022 has been supplied with this report.</p></div>
  <div class="map" role="img" aria-label="Street map showing the property location beside the lake"></div>
  <div class="sat" role="img" aria-label="Aerial satellite view of the property and surrounding streets"></div>
  <div class="page-foot">[[StreetAddress]] [[Suburb]] - COPYRIGHT: Keystone Survey<span class="page-num">Page 3</span></div>
</section>

<!-- Page 4 -->
<section class="page page--land" style="left:50px;top:402px">
  <div class="page-head"><div class="page-logo">Keystone<br>Survey</div><div class="page-title">ACT Maintenance Plan - 2022</div></div>
  <div class="sec" style="top:43px">
    <div class="sec-title">GENERAL OBSERVATIONS SUMMARY</div>
    <p class="body-text">The preparation of this Maintenance Plan included a full on-site inspection where all building elements noted in the plan were reviewed to determine life cycles and continuity of service. While the purpose of a maintenance plan is not to address defects, any observations noted by the inspector are listed below as a courtesy. Please note we cannot guarantee all defects have been listed and strongly recommend the Routine/Safety inspections for each building element detailed in the plan are followed.<br><b>Please refer to our Scope &amp; Limitations at the end of this document.</b></p>
    <table class="grid-table" style="margin-top:4px">
      <colgroup><col style="width:9%"><col style="width:16%"><col style="width:18%"><col></colgroup>
      <tr><th>DATE</th><th>OBSERVATION</th><th>INSPECTOR</th><th>DETAILS</th></tr>
      <tr><td></td><td></td><td></td><td></td></tr><tr><td></td><td></td><td></td><td></td></tr>
      <tr><td></td><td></td><td></td><td></td></tr><tr><td></td><td></td><td></td><td></td></tr>
    </table>
  </div>
  <div class="sec" style="top:117px">
    <div class="sec-title">NEXT ACTION PLAN</div>
    <p class="body-text">To assist with future planning, inspections recommended over the upcoming 18 months are detailed below:</p>
    <table class="grid-table" style="margin-top:3px">
      <colgroup><col style="width:18%"><col style="width:18%"><col style="width:15%"><col></colgroup>
      <tr><th>BUILDING ELEMENT</th><th>NEXT INSPECTION DUE</th><th>TYPE</th><th>WHO?</th></tr>
      <tr><td></td><td></td><td></td><td></td></tr><tr><td></td><td></td><td></td><td></td></tr>
      <tr><td></td><td></td><td></td><td></td></tr>
    </table>
  </div>
  <div class="sec" style="top:182px">
    <table class="grid-table">
      <colgroup><col style="width:31%"><col span="16"></colgroup>
      <tr><td colspan="17">Estimated Service Life Summary (indicates where anticipated next investment – other than a routine service/repair – is projected)</td></tr>
      <tr><td></td><td>2022</td><td>2023</td><td>2024</td><td>2025</td><td>2026</td><td>2027</td><td>2028</td><td>2029</td><td>2030</td><td>2031</td><td>2032</td><td>2033</td><td>2034</td><td>2035</td><td>2036</td><td>2037</td></tr>
      <tr><td>Superstructure - Repaint Buildings</td><td></td><td></td><td></td><td></td><td></td><td></td><td></td><td></td><td></td><td></td><td></td><td></td><td></td><td></td><td></td><td></td></tr>
      <tr><td>Superstructure - Repaint Balcony/Patio Ceilings</td><td></td><td></td><td></td><td></td><td></td><td></td><td></td><td></td><td></td><td></td><td></td><td></td><td></td><td></td><td></td><td></td></tr>
    </table>
  </div>
  <div class="page-foot">[[StreetAddress]] [[Suburb]] - COPYRIGHT: Keystone Survey<span class="page-num">Page 4</span></div>
</section>

<!-- Page 5 -->
<section class="page page--land" style="left:392px;top:402px">
  <div class="page-head"><div class="page-logo">Keystone<br>Survey</div><div class="page-title" style="left:64px;right:auto">ACT Maintenance Plan - 2022</div></div>
  <div class="super">
    <div class="super-title">SUPERSTRUCTURE</div>
    <div class="super-row"><span>INSPECTOR:</span><span>Keystone Survey</span></div>
    <div class="super-row"><span>INSPECTION TYPE:</span><span>Routine</span></div>
    <div class="super-row"><span>INSPECTION FREQUENCY:</span><span>Annual</span></div>
    <div class="super-row"><span>LAST INSPECTION DATE:</span><span>2/5/2022</span></div>
    <div class="super-row"><span>NEXT INSPECTION DATE:</span><span>2/5/2023</span></div>
  </div>
  <div class="sec" style="top:50px">
    <div class="sec-title">INSPECTION TYPES</div>
    <dl class="defs">
      <dt>ROUTINE</dt><dd>General inspection to determine that the building element is in acceptable order showing no signs of deterioration or damage that may require attention or repair</dd>
      <dt>ROUTINE/SAFETY</dt><dd>Following the guidelines of a routine inspection with a particular focus on items that may cause injury to owners/occupants/visitors</dd>
      <dt>SERVICE</dt><dd>An inspection where some additional level of attention or maintenance may be required, e.g. cleaning a pool filter</dd>
      <dt>OPERATIONAL</dt><dd>Inspection to ascertain the element is operational</dd>
      <dt>COMPLIANCE</dt><dd>Inspect, test and maintain as required to ensure the building element meets a particular Regulation or Standard</dd>
      <dt>SANITATION</dt><dd>Required Health &amp; Safety check for residents</dd>
    </dl>
  </div>
  <div class="sec" style="top:102px">
    <div class="sec-title">REPAINT BUILDING EXTERIOR</div>
    <table class="grid-table grid-table--teal">
      <colgroup><col style="width:19%"><col style="width:20%"><col style="width:17%"><col></colgroup>
      <tr><th>MAKE/MODEL</th><th>IDENTIFIER</th><th>INSTALL DATE</th><th>RELEVANT STANDARD</th></tr>
      <tr><td>Paintco 29/1/2022</td><td></td><td>Assume early 2022</td><td></td></tr>
    </table>
    <div class="life" style="margin-top:3px">
      <div class="life-head"><b>ESTIMATED SERVICE LIFESPAN</b><i>2022</i><i>2023</i><i>2024</i><i>2025</i><i>2026</i><i>2027</i><i>2028</i><i>2029</i><i>2030</i><i>2031</i><i>2032</i><i>2033</i><i>2034</i><i>2035</i><i>2036</i><i>2037</i></div>
      <p class="life-note">Forecast year when major refurbishment or replacement may be needed for each item. Where a Sinking Fund exists, this may show forecast spending.</p>
      <div class="life-row"><b>10 YEARS</b><i></i><i></i><i></i><i></i><i></i><i></i><i class="tick"></i><i></i><i></i><i></i><i></i><i></i><i></i><i></i><i></i><i></i></div>
    </div>
    <p class="label">General observations during Maintenance Plan review</p>
    <table class="grid-table">
      <colgroup><col style="width:11%"><col style="width:16%"><col style="width:19%"><col></colgroup>
      <tr><th>DATE</th><th>TYPE</th><th>INSPECTOR</th><th>OBSERVATION</th></tr>
      <tr><td>2/5/2022</td><td>Maintenance</td><td>Keystone Survey</td><td>Exterior of building adjacent to gymnasium requires painting</td></tr>
      <tr><td>2/5/2022</td><td>Maintenance</td><td>Keystone Survey</td><td>Exterior of building adjacent to guest recreation room requires repainting</td></tr>
      <tr><td>2/5/2022</td><td>Observation</td><td>Keystone Survey</td><td>Paintco paint observed in basement, clearly used for some external surfaces, but not a full building repaint</td></tr>
    </table>
    <p class="label">Service/Routine Inspection History</p>
    <table class="grid-table">
      <colgroup><col style="width:8%"><col style="width:21%"><col style="width:15%"><col style="width:8%"><col style="width:30%"><col></colgroup>
      <tr><th>DATE</th><th>COMPANY</th><th>TYPE</th><th>COST</th><th>DETAILS</th><th>RECEIPT/WARRANTY LOGGED IN STRATAVAULT</th></tr>
      <tr><td>2018</td><td>Unknown</td><td>Repaint Building</td><td>$136,118</td><td>Identified in Sinking Fund (prepared July 18 2017)</td><td>N</td></tr>
    </table>
  </div>
  <div class="page-foot">[[StreetAddress]] [[Suburb]] - COPYRIGHT: Keystone Survey<span class="page-num">Page 5</span></div>
</section>

<!-- Page 6 -->
<section class="page page--land" style="left:733px;top:402px">
  <div class="page-head"><div class="page-logo">Keystone<br>Survey</div><div class="page-title">ACT Maintenance Plan - 2022</div></div>
  <div class="sec" style="top:55px">
    <div class="sec-title">REPAINT SOFFITS</div>
    <div class="life">
      <div class="life-head"><b>ESTIMATED SERVICE LIFESPAN</b><i>2022</i><i>2023</i><i>2024</i><i>2025</i><i>2026</i><i>2027</i><i>2028</i><i>2029</i><i>2030</i><i>2031</i><i>2032</i><i>2033</i><i>2034</i><i>2035</i><i>2036</i><i>2037</i></div>
      <p class="life-note">Forecast year when major refurbishment or replacement may be needed for each item. Where a Sinking Fund exists, this may show forecast spending.</p>
      <div class="life-row"><b>10 YEARS</b><i></i><i></i><i></i><i></i><i></i><i></i><i class="tick"></i><i></i><i></i><i></i><i></i><i></i><i></i><i></i><i></i><i></i></div>
    </div>
    <p class="label">General observations during Maintenance Plan review</p>
    <table class="grid-table">
      <colgroup><col style="width:11%"><col style="width:17%"><col style="width:19%"><col></colgroup>
      <tr><th>DATE</th><th>TYPE</th><th>INSPECTOR</th><th>OBSERVATION</th></tr>
      <tr><td>2/5/2022</td><td>Maintenance</td><td>Keystone Survey</td><td>Flaking paint was observed to balcony ceilings below the old pool area</td></tr>
    </table>
    <p class="label">Service/Routine Inspection History</p>
    <table class="grid-table">
      <colgroup><col style="width:8%"><col style="width:21%"><col style="width:15%"><col style="width:8%"><col style="width:30%"><col></colgroup>
      <tr><th>DATE</th><th>COMPANY</th><th>TYPE</th><th>COST</th><th>DETAILS</th><th>RECEIPT/WARRANTY LOGGED IN STRATAVAULT</th></tr>
      <tr><td>2018</td><td>Unknown</td><td>Repaint verandah ceilings</td><td>$32,895</td><td>Identified in Sinking Fund (prepared July 18 2017)</td><td>N</td></tr>
    </table>
  </div>
  <div class="sec" style="top:158px">
    <div class="sec-title">REPAIR/MAINTAIN COMMON AREA WINDOW COVERINGS</div>
    <div class="life">
      <div class="life-head"><b>ESTIMATED SERVICE LIFESPAN</b><i>2022</i><i>2023</i><i>2024</i><i>2025</i><i>2026</i><i>2027</i><i>2028</i><i>2029</i><i>2030</i><i>2031</i><i>2032</i><i>2033</i><i>2034</i><i>2035</i><i>2036</i><i>2037</i></div>
      <p class="life-note">Forecast year when major refurbishment or replacement may be needed for each item. Where a Sinking Fund exists, this may show forecast spending.</p>
      <div class="life-row"><b>10 YEARS</b><i></i><i></i><i></i><i></i><i></i><i></i><i class="tick"></i><i></i><i></i><i></i><i></i><i></i><i></i><i></i><i></i><i></i></div>
    </div>
  </div>
  <div class="page-foot">[[StreetAddress]] [[Suburb]] - COPYRIGHT: Keystone Survey<span class="page-num">Page 6</span></div>
</section>

<!-- Page 7 (windows) -->
<section class="page page--land" style="left:50px;top:656px">
  <div class="page-head"><div class="page-logo">Keystone<br>Survey</div><div class="page-title">ACT Maintenance Plan - 2022</div></div>
  <div class="sec" style="top:58px">
    <div class="sec-title">REPAIR/MAINTAIN WINDOWS</div>
    <div class="life">
      <div class="life-head"><b>ESTIMATED SERVICE LIFESPAN</b><i>2022</i><i>2023</i><i>2024</i><i>2025</i><i>2026</i><i>2027</i><i>2028</i><i>2029</i><i>2030</i><i>2031</i><i>2032</i><i>2033</i><i>2034</i><i>2035</i><i>2036</i><i>2037</i></div>
      <p class="life-note">Forecast year when major refurbishment or replacement may be needed for each item. Where a Sinking Fund exists, this may show forecast spending.</p>
      <div class="life-row"><b>5 YEARS</b><i></i><i></i><i></i><i></i><i class="tick"></i><i></i><i></i><i></i><i></i><i></i><i></i><i></i><i></i><i></i><i></i><i></i></div>
    </div>
    <p class="label">General observations during Maintenance Plan review</p>
    <table class="grid-table">
      <colgroup><col style="width:10%"><col style="width:16%"><col style="width:18%"><col></colgroup>
      <tr><th>DATE</th><th>TYPE</th><th>INSPECTOR</th><th>OBSERVATION</th></tr>
      <tr><td>2/5/2022</td><td>Maintenance</td><td>Keystone Survey</td><td>The window sill to a window adjacent to the outdoor recreation areas has deteriorated and requires repairs or replacement</td></tr>
    </table>
    <p class="label">Service/Routine Inspection History</p>
    <table class="grid-table">
      <colgroup><col style="width:7%"><col style="width:21%"><col style="width:15%"><col style="width:7%"><col style="width:30%"><col></colgroup>
      <tr><th>DATE</th><th>COMPANY</th><th>TYPE</th><th>COST</th><th>DETAILS</th><th>RECEIPT/WARRANTY LOGGED IN STRATAVAULT</th></tr>
      <tr><td>2021</td><td>Unknown</td><td>Maintain Window Fixtures &amp; Fittings</td><td>$12,520</td><td>Identified in Sinking Fund (prepared July 18 2017)</td><td>N</td></tr>
    </table>
  </div>
  <div class="page-foot">[[StreetAddress]] [[Suburb]] - COPYRIGHT: Keystone Survey<span class="page-num">Page 7</span></div>
</section>

<!-- Page 6 variant -->
<section class="page page--land" style="left:392px;top:656px">
  <div class="page-head"><div class="page-logo">Keystone<br>Survey</div><div class="page-title">ACT Maintenance Plan - 2022</div></div>
  <div class="sec" style="top:54px">
    <div class="sec-title">REPAINT SOFFITS</div>
    <div class="life">
      <div class="life-head"><b>ESTIMATED SERVICE LIFESPAN</b><i>2022</i><i>2023</i><i>2024</i><i>2025</i><i>2026</i><i>2027</i><i>2028</i><i>2029</i><i>2030</i><i>2031</i><i>2032</i><i>2033</i><i>2034</i><i>2035</i><i>2036</i><i>2037</i></div>
      <p class="life-note">Forecast year when major refurbishment or replacement may be needed for each item. Where a Sinking Fund exists, this may show forecast spending.</p>
      <div class="life-row"><b>10 YEARS</b><i></i><i></i><i></i><i></i><i></i><i></i><i class="tick"></i><i></i><i></i><i></i><i></i><i></i><i></i><i></i><i></i><i></i></div>
    </div>
    <p class="label">General observations during Maintenance Plan review</p>
    <table class="grid-table">
      <colgroup><col style="width:11%"><col style="width:16%"><col style="width:19%"><col></colgroup>
      <tr><th>DATE</th><th>TYPE</th><th>INSPECTOR</th><th>OBSERVATION</th></tr>
      <tr><td>2/5/2022</td><td>Maintenance</td><td>Keystone Survey</td><td>Flaking paint was observed to balcony ceilings below the old pool area</td></tr>
    </table>
    <p class="label">Service/Routine Inspection History</p>
    <table class="grid-table">
      <colgroup><col style="width:8%"><col style="width:21%"><col style="width:15%"><col style="width:8%"><col style="width:30%"><col></colgroup>
      <tr><th>DATE</th><th>COMPANY</th><th>TYPE</th><th>COST</th><th>DETAILS</th><th>RECEIPT/WARRANTY LOGGED IN STRATAVAULT</th></tr>
      <tr><td>2018</td><td>Unknown</td><td>Repaint verandah ceilings</td><td>$32,895</td><td>Identified in Sinking Fund (prepared July 18 2017)</td><td>N</td></tr>
    </table>
  </div>
  <div class="sec" style="top:158px">
    <div class="sec-title">REPAIR/MAINTAIN COMMON AREA WINDOW COVERINGS</div>
    <div class="life">
      <div class="life-head"><b>ESTIMATED SERVICE LIFESPAN</b><i>2022</i><i>2023</i><i>2024</i><i>2025</i><i>2026</i><i>2027</i><i>2028</i><i>2029</i><i>2030</i><i>2031</i><i>2032</i><i>2033</i><i>2034</i><i>2035</i><i>2036</i><i>2037</i></div>
      <p class="life-note">Forecast year when major refurbishment or replacement may be needed for each item. Where a Sinking Fund exists, this may show forecast spending.</p>
      <div class="life-row"><b>10 YEARS</b><i></i><i></i><i></i><i></i><i></i><i></i><i class="tick"></i><i></i><i></i><i></i><i></i><i></i><i></i><i></i><i></i><i></i></div>
    </div>
  </div>
  <div class="page-foot">[[StreetAddress]] [[Suburb]] - COPYRIGHT: Keystone Survey<span class="page-num">Page 6</span></div>
</section>

<!-- Page 7 variant -->
<section class="page page--land" style="left:733px;top:656px">
  <div class="page-head"><div class="page-logo">Keystone<br>Survey</div><div class="page-title">ACT Maintenance Plan - 2022</div></div>
  <div class="sec" style="top:54px">
    <div class="sec-title">REPAIR/MAINTAIN WINDOWS</div>
    <div class="life">
      <div class="life-head"><b>ESTIMATED SERVICE LIFESPAN</b><i>2022</i><i>2023</i><i>2024</i><i>2025</i><i>2026</i><i>2027</i><i>2028</i><i>2029</i><i>2030</i><i>2031</i><i>2032</i><i>2033</i><i>2034</i><i>2035</i><i>2036</i><i>2037</i></div>
      <p class="life-note">Forecast year when major refurbishment or replacement may be needed for each item. Where a Sinking Fund exists, this may show forecast spending.</p>
      <div class="life-row"><b>5 YEARS</b><i></i><i></i><i></i><i></i><i class="tick"></i><i></i><i></i><i></i><i></i><i></i><i></i><i></i><i></i><i></i><i></i><i></i></div>
    </div>
    <p class="label">General observations during Maintenance Plan review</p>
    <table class="grid-table">
      <colgroup><col style="width:10%"><col style="width:16%"><col style="width:19%"><col></colgroup>
      <tr><th>DATE</th><th>TYPE</th><th>INSPECTOR</th><th>OBSERVATION</th></tr>
      <tr><td>2/5/2022</td><td>Maintenance</td><td>Keystone Survey</td><td>The window sill to a window adjacent to the outdoor recreation areas has deteriorated and requires repairs or replacement</td></tr>
    </table>
    <p class="label">Service/Routine Inspection History</p>
    <table class="grid-table">
      <colgroup><col style="width:8%"><col style="width:21%"><col style="width:15%"><col style="width:8%"><col style="width:30%"><col></colgroup>
      <tr><th>DATE</th><th>COMPANY</th><th>TYPE</th><th>COST</th><th>DETAILS</th><th>RECEIPT/WARRANTY LOGGED IN STRATAVAULT</th></tr>
      <tr><td>2021</td><td>Unknown</td><td>Maintain Window Fixtures &amp; Fittings</td><td>$12,520</td><td>Identified in Sinking Fund (prepared July 18 2017)</td><td>N</td></tr>
    </table>
  </div>
  <div class="sec" style="top:157px">
    <div class="sec-title">MAINTAIN BALCONY/PATIO/ENTRY FLOOR TILES</div>
    <div class="life">
      <div class="life-head"><b>ESTIMATED SERVICE LIFESPAN</b><i>2022</i><i>2023</i><i>2024</i><i>2025</i><i>2026</i><i>2027</i><i>2028</i><i>2029</i><i>2030</i><i>2031</i><i>2032</i><i>2033</i><i>2034</i><i>2035</i><i>2036</i><i>2037</i></div>
      <p class="life-note">Forecast year when major refurbishment or replacement may be needed for each item. Where a Sinking Fund exists, this may show forecast spending.</p>
      <div class="life-row"><b>10 YEARS</b><i></i><i></i><i></i><i></i><i></i><i></i><i class="tick"></i><i></i><i></i><i></i><i></i><i></i><i></i><i></i><i></i><i></i></div>
    </div>
    <p class="label">General observations during Maintenance Plan review</p>
    <table class="grid-table">
      <colgroup><col style="width:10%"><col style="width:16%"><col style="width:19%"><col></colgroup>
      <tr><th>DATE</th><th>TYPE</th><th>INSPECTOR</th><th>OBSERVATION</th></tr>
      <tr><td>2/5/2022</td><td>Maintenance</td><td>Keystone Survey</td><td>Some areas of foyer floor tiling require grout repairs</td></tr>
    </table>
  </div>
  <div class="page-foot">[[StreetAddress]] [[Suburb]] - COPYRIGHT: Keystone Survey<span class="page-num">Page 7</span></div>
</section>

<!-- Page 8 -->
<section class="page page--land" style="left:50px;top:912px">
  <div class="page-head"><div class="page-logo">Keystone<br>Survey</div><div class="page-title">ACT Maintenance Plan - 2022</div></div>
  <div class="sec" style="top:51px">
    <div class="sec-title">REPAINT BALUSTRADES &amp; HANDRAILS</div>
    <div class="life">
      <div class="life-head"><b>ESTIMATED SERVICE LIFESPAN</b><i>2022</i><i>2023</i><i>2024</i><i>2025</i><i>2026</i><i>2027</i><i>2028</i><i>2029</i><i>2030</i><i>2031</i><i>2032</i><i>2033</i><i>2034</i><i>2035</i><i>2036</i><i>2037</i></div>
      <p class="life-note">Forecast year when major refurbishment or replacement may be needed for each item. Where a Sinking Fund exists, this may show forecast spending.</p>
      <div class="life-row"><b>5 YEARS</b><i></i><i class="tick"></i><i></i><i></i><i></i><i></i><i></i><i></i><i></i><i></i><i></i><i></i><i></i><i></i><i></i><i></i></div>
    </div>
  </div>
  <div class="sec" style="top:97px">
    <div class="sec-title">REPAIR/MAINTAIN BALUSTRADE &amp; HANDRAIL FIXINGS</div>
    <div class="life">
      <div class="life-head"><b>ESTIMATED SERVICE LIFESPAN</b><i>2022</i><i>2023</i><i>2024</i><i>2025</i><i>2026</i><i>2027</i><i>2028</i><i>2029</i><i>2030</i><i>2031</i><i>2032</i><i>2033</i><i>2034</i><i>2035</i><i>2036</i><i>2037</i></div>
      <p class="life-note">Forecast year when major refurbishment or replacement may be needed for each item. Where a Sinking Fund exists, this may show forecast spending.</p>
      <div class="life-row"><b>20 YEARS</b><i></i><i></i><i></i><i></i><i></i><i></i><i></i><i></i><i></i><i></i><i class="tick"></i><i></i><i></i><i></i><i></i><i></i></div>
    </div>
  </div>
  <div class="sec" style="top:142px">
    <div class="sec-title">REPAIR/MAINTAIN WATERPROOFING</div>
    <div class="life">
      <div class="life-head"><b>ESTIMATED SERVICE LIFESPAN</b><i>2022</i><i>2023</i><i>2024</i><i>2025</i><i>2026</i><i>2027</i><i>2028</i><i>2029</i><i>2030</i><i>2031</i><i>2032</i><i>2033</i><i>2034</i><i>2035</i><i>2036</i><i>2037</i></div>
      <p class="life-note">Forecast year when major refurbishment or replacement may be needed for each item. Where a Sinking Fund exists, this may show forecast spending.</p>
      <div class="life-row"><b>10 YEARS</b><i></i><i></i><i></i><i></i><i></i><i class="tick"></i><i></i><i></i><i></i><i></i><i></i><i></i><i></i><i></i><i></i><i></i></div>
    </div>
    <p class="label">Service/Routine Inspection History</p>
    <table class="grid-table">
      <colgroup><col style="width:7%"><col style="width:21%"><col style="width:15%"><col style="width:8%"><col style="width:30%"><col></colgroup>
      <tr><th>DATE</th><th>COMPANY</th><th>TYPE</th><th>COST</th><th>DETAILS</th><th>RECEIPT/WARRANTY LOGGED IN STRATAVAULT</th></tr>
      <tr><td>2017</td><td>Unknown</td><td>Building Waterproofing repairs</td><td>$41,659</td><td>Identified in Sinking Fund (prepared July 18 2017)</td><td>N</td></tr>
    </table>
  </div>
  <div class="page-foot">[[StreetAddress]] [[Suburb]] - COPYRIGHT: Keystone Survey<span class="page-num">Page 8</span></div>
</section>

<!-- Page 9 -->
<section class="page page--land" style="left:392px;top:912px">
  <div class="page-head"><div class="page-logo">Keystone<br>Survey</div><div class="page-title">ACT Maintenance Plan - 2022</div></div>
  <div class="sec" style="top:51px">
    <div class="sec-title">REPAIR/MAINTAIN BALCONY MEMBRANE</div>
    <div class="life">
      <div class="life-head"><b>ESTIMATED SERVICE LIFESPAN</b><i>2022</i><i>2023</i><i>2024</i><i>2025</i><i>2026</i><i>2027</i><i>2028</i><i>2029</i><i>2030</i><i>2031</i><i>2032</i><i>2033</i><i>2034</i><i>2035</i><i>2036</i><i>2037</i></div>
      <p class="life-note">Forecast year when major refurbishment or replacement may be needed for each item. Where a Sinking Fund exists, this may show forecast spending.</p>
      <div class="life-row"><b>5 YEARS</b><i></i><i></i><i class="tick"></i><i></i><i></i><i></i><i></i><i></i><i></i><i></i><i></i><i></i><i></i><i></i><i></i><i></i></div>
    </div>
    <p class="label">Service/Routine Inspection History</p>
    <table class="grid-table">
      <colgroup><col style="width:8%"><col style="width:21%"><col style="width:15%"><col style="width:8%"><col style="width:30%"><col></colgroup>
      <tr><th>DATE</th><th>COMPANY</th><th>TYPE</th><th>COST</th><th>DETAILS</th><th>RECEIPT/WARRANTY LOGGED IN STRATAVAULT</th></tr>
      <tr><td>2019</td><td>Unknown</td><td>Maintain roof</td><td>$60,187</td><td>Identified in Sinking Fund (prepared July 18 2017)</td><td>N</td></tr>
    </table>
  </div>
  <div class="sec" style="top:130px">
    <div class="sec-title">REPAIR/MAINTAIN ROOF</div>
    <div class="life">
      <div class="life-head"><b>ESTIMATED SERVICE LIFESPAN</b><i>2022</i><i>2023</i><i>2024</i><i>2025</i><i>2026</i><i>2027</i><i>2028</i><i>2029</i><i>2030</i><i>2031</i><i>2032</i><i>2033</i><i>2034</i><i>2035</i><i>2036</i><i>2037</i></div>
      <p class="life-note">Forecast year when major refurbishment or replacement may be needed for each item. Where a Sinking Fund exists, this may show forecast spending.</p>
      <div class="life-row"><b>10 YEARS</b><i></i><i></i><i></i><i></i><i></i><i class="tick"></i><i></i><i></i><i></i><i></i><i></i><i></i><i></i><i></i><i></i><i></i></div>
    </div>
  </div>
  <div class="sec" style="top:176px">
    <div class="sec-title">REPAIR/MAINTAIN SKYLIGHTS</div>
    <div class="life">
      <div class="life-head"><b>ESTIMATED SERVICE LIFESPAN</b><i>2022</i><i>2023</i><i>2024</i><i>2025</i><i>2026</i><i>2027</i><i>2028</i><i>2029</i><i>2030</i><i>2031</i><i>2032</i><i>2033</i><i>2034</i><i>2035</i><i>2036</i><i>2037</i></div>
      <p class="life-note">Forecast year when major refurbishment or replacement may be needed for each item. Where a Sinking Fund exists, this may show forecast spending.</p>
      <div class="life-row"><b>10 YEARS</b><i></i><i></i><i class="tick"></i><i></i><i></i><i></i><i></i><i></i><i></i><i></i><i></i><i></i><i></i><i></i><i></i><i></i></div>
    </div>
  </div>
  <div class="page-foot">[[StreetAddress]] [[Suburb]] - COPYRIGHT: Keystone Survey<span class="page-num">Page 9</span></div>
</section>

</main>
</body>
</html>
```